Indian Lunch Delivery company needs a google ad banner for advertising its offering

We are a Kolkata, India based startup delivering lunch to office buildings in the city. We only serve set meals (vegetarian and non-vegetarian). Minimum order quantity is 5 boxes. The name of the brand is Verdopan (Thali=platter). Our USP-
We cook fresh
Trans-fat free
No emulsifiers, preservatives or artificial colorings used.
Importantly, we are a value for money brand. To be precise our meals costs just .99 c.
Target Market(s)
Young professionals
Industry/Entity Type
It Company
Font styles to use
Sans Serif
Requirements
Must have
- Home made food feel to it
Nice to have
- Lots of colours

```html
<!DOCTYPE html>
<html lang="en">
<head>
<meta charset="utf-8">
<title>Verdopan – Lunch Delivery Banner</title>
<link rel="stylesheet" href="https://fonts.googleapis.com/css2?family=Oswald:wght@300&family=Kalam:wght@400&family=Libre+Baskerville:ital@1&display=swap">
<style>
  :root {
    --bg: #000000;
    --frame: #4a4a4a;
    --white: #ffffff;
    --mint: #5ec6a2;
    --photo-rice: #e9e4d6;
    --photo-curry: #b8441a;
    --photo-deep: #5a1a08;
  }
  html, body {
    margin: 0;
    padding: 0;
    overflow: hidden;
    background: var(--bg);
  }
  .banner {
    position: relative;
    width: 1200px;
    height: 232px;
    background: var(--bg);
    overflow: hidden;
  }
  .tagline-box {
    position: absolute;
    left: 30px;
    top: 28px;
    width: 338px;
    height: 175px;
    box-sizing: border-box;
    border: 1px solid var(--frame);
    display: flex;
    flex-direction: column;
    justify-content: center;
    padding-left: 17px;
  }
  .tagline {
    margin: 0;
    font-family: "Oswald", sans-serif;
    font-weight: 300;
    font-size: 30px;
    line-height: 44px;
    color: var(--white);
    letter-spacing: 0.3px;
  }
  .tagline span { display: block; }
  .tagline .second { padding-left: 8px; }
  .delivery-button {
    position: absolute;
    left: 419px;
    top: 66px;
    width: 242px;
    height: 82px;
    background: var(--mint);
    border-radius: 4px;
    display: flex;
    flex-direction: column;
    align-items: center;
    justify-content: center;
    color: var(--white);
    font-family: "Kalam", sans-serif;
  }
  .delivery-label {
    font-size: 16px;
    line-height: 20px;
    font-style: italic;
    letter-spacing: 1px;
  }
  .delivery-phone {
    font-size: 24px;
    line-height: 30px;
    font-style: italic;
    letter-spacing: 1.5px;
  }
  .website {
    position: absolute;
    left: 419px;
    top: 158px;
    width: 242px;
    text-align: center;
    font-family: "Libre Baskerville", serif;
    font-style: italic;
    font-size: 21px;
    color: var(--white);
    margin: 0;
  }
  .meal-photo {
    position: absolute;
    left: 693px;
    top: 0;
    width: 507px;
    height: 232px;
    background:
      radial-gradient(ellipse at 22% 60%, var(--photo-rice) 0%, rgba(233,228,214,0.6) 22%, transparent 42%),
      radial-gradient(ellipse at 50% 80%, var(--photo-curry) 0%, rgba(184,68,26,0.7) 28%, transparent 50%),
      radial-gradient(ellipse at 90% 35%, #d9652c 0%, rgba(217,101,44,0.6) 25%, transparent 45%),
      linear-gradient(100deg, #2e1e14 0%, var(--photo-deep) 55%, #3a1a0c 100%);
  }
</style>
</head>
<body>
  <main class="banner">
    <section class="tagline-box">
      <h1 class="tagline">
        <span class="first">RECIPES FOR SIMPLE</span>
        <span class="second">&amp; HEALTHY EATING</span>
      </h1>
    </section>

    <div class="delivery-button">
      <span class="delivery-label">DELIVERY CALL</span>
      <span class="delivery-phone">91 9000 5555 21</span>
    </div>

    <p class="website">www.verdopan.com</p>

    <div class="meal-photo" role="img" aria-label="Photo of an Indian set meal: bowl of rice with green peas, bowls of red curry garnished with coriander, lime wedge and naan bread"></div>
  </main>
</body>
</html>
```